Commercial/Corporate Law Firm needs Website Design

Hi guys. I've started up a new law firm and would love your help designing an attractive website. I'll need both design and coding, and to make it easy for us to edit as necessary later, I think it should be built off a Wordpress.org structure.
FIRST IMPRESSIONS
It's very important that the first impression of the website really captures our prospective clients' attention and impresses them. Their first three seconds needs to be good.
I imagine the homepage may be short, with a menu bar and a compelling image, and with a tagline overlaid or underneath (eg. "It's about results.")
The image should be related to our practice areas: eg. IPOs, corporate transactions, or commercial negotiations.
I have previously suggested there could be a skyline image of Sydney or Adelaide. However, because we are based in Adelaide, I don't think Sydney is appropriate - and Adelaide is probably too boring to use.
HOMEPAGE
Being a new firm, we don't have many existing testimonials, and I will be the only lawyer to start with. So we need to focus on the nature of the services we will provide and how my experience can help them. We have an existing logo to use, and I would like the website colour scheme not to clash with that logo (dark blue and white).
After the initial image and tagline there should be a brief introduction to each of the main areas of work, eg. "We specialise in three main areas of practice:"
1. Corporate Transactions and Regulation
2. Business Law and Dispute Resolution
3. Migration Assistance
These should each have an appropriate photo and link to a separate page that briefly describes our services in that area.
Below that there should be a message from me with a photo. Finally, at the bottom, there should be a "Contact Us" section which shows a Google image of our address, contact details, and then our logo with colours inverted.
OTHER PAGES
While we will need some other pages, they should all be fairly simple. I think we will need one page to say "About Us", where I will put information about my experience. I think we will then need one page for each of the 3 areas listed above, which just needs an appropriate image and then text to describe the service. Finally, a "Contact Us" page which I imagine will be the same as the bottom of the homepage.
OTHER DETAILS
For now you can use details from my LinkedIn page to fill out any other text as necessary, or the photo.
Because the logo is square, I would prefer the design of the website also to be rectangular.
Looking forward to seeing your work! Thank you.
Good luck,
Marcus
Target Market(s)
Potential clients:
Businesses with legal issues or disputes
Companies wishing to list on the stock market

```html
<!DOCTYPE html>
<html lang="en">
<head>
<meta charset="utf-8">
<title>Corvell Legal</title>
<link href="https://fonts.googleapis.com/css2?family=Montserrat:wght@500;600;700&family=Roboto:wght@300;400;500;700;900&display=swap" rel="stylesheet">
<style>
:root{
  --navy:#1d3660;
  --navy-deep:#152a4c;
  --sky:#3ba7e0;
  --ink:#1d3660;
  --muted:#8b93a3;
  --light:#c9d3e3;
  --white:#ffffff;
  --map:#3b3b3d;
  --line:#c7ccd5;
}
*{margin:0;padding:0;box-sizing:border-box}
html,body{width:1200px;height:3114px;overflow:hidden}
body{position:relative;background:var(--white);font-family:"Roboto",Arial,sans-serif;color:var(--ink)}
.abs{position:absolute}
a{color:inherit;text-decoration:none}

/* header */
.site-header{left:0;top:0;width:1200px;height:83px;background:var(--navy);z-index:5}
.brand{left:253px;top:16px;width:92px;display:flex;flex-direction:column;align-items:center;gap:5px;color:var(--white);font-family:"Montserrat",sans-serif;font-weight:600;font-size:10.5px;letter-spacing:1.2px;white-space:nowrap}
.brand-mark{width:24px;height:24px;background:var(--white)}
.main-nav{font-family:"Montserrat",sans-serif;font-size:11px;font-weight:600;color:var(--white)}
.main-nav a{position:absolute;white-space:nowrap}
.main-nav .current::after{content:"";position:absolute;left:-12px;right:-12px;bottom:-9px;height:2px;background:var(--white)}
.cta-start{left:826px;top:27px;width:119px;height:26px;border-radius:13px;background:var(--white);color:var(--navy);font-family:"Montserrat",sans-serif;font-size:9.5px;font-weight:700;display:flex;align-items:center;justify-content:center}

/* hero */
.hero-art{left:0;top:83px}
.hero-copy{left:255px;top:238px;color:var(--white)}
.hero-kicker{font-family:"Montserrat",sans-serif;font-size:13px;font-weight:500}
.hero-title{font-family:"Montserrat",sans-serif;font-size:33px;font-weight:600;letter-spacing:.5px;margin-top:4px;line-height:38px}
.hero-tag{font-family:"Montserrat",sans-serif;font-size:18px;font-weight:600;color:var(--sky);letter-spacing:1px}
.hero-text{width:330px;font-size:10px;line-height:13.5px;color:#dfe6f0;margin-top:8px}
.btn{display:flex;align-items:center;justify-content:center;border-radius:14px;font-family:"Montserrat",sans-serif;font-size:9px;font-weight:700;letter-spacing:.4px;height:26px;white-space:nowrap}
.btn-solid{background:var(--navy);color:var(--white)}
.btn-ghost{border:1.5px solid var(--white);color:var(--white)}

/* about */
.eyebrow{font-size:10px;color:var(--muted);letter-spacing:.4px}
.about-title{left:264px;top:640px;font-family:"Montserrat",sans-serif;font-weight:700;font-size:24px;line-height:29px}
.about-title .accent{color:var(--sky)}
.about-text{left:554px;top:640px;width:380px;font-size:11px;line-height:17px;color:#9aa2b2;font-weight:300}

/* services */
.services-band{left:0;top:780px}
.services-head{left:0;top:926px;width:1200px;text-align:center;color:var(--white)}
.services-head .eyebrow{color:#c3cce0}
.services-head h2{font-weight:900;font-size:40px;margin-top:4px}
.service-grid{left:243px;top:1021px;width:714px;height:357px;display:grid;grid-template-columns:238px 238px 238px;grid-template-rows:178.5px 178.5px}
.service-photo{width:100%;height:100%}
.service-card{color:var(--white);text-align:center;padding:52px 24px 0}
.service-card h3{font-size:10.5px;font-weight:700}
.service-card p{font-size:9.5px;line-height:13px;color:#aab5cc;margin-top:12px}
.services-more{left:533px;top:1440px;width:132px;height:26px}

/* message */
.message-frame{left:218px;top:1675px;width:355px;height:328px;background:var(--navy)}
.message-photo{left:243px;top:1702px;width:359px;height:337px;background:radial-gradient(circle at 80% 60%,#e0a04e 0,#6d4a2f 18%,transparent 40%),linear-gradient(160deg,#2a3550 0%,#1a2035 45%,#3b2a22 100%);box-shadow:0 6px 18px rgba(0,0,0,.25)}
.quote-mark{left:631px;top:1786px}
.message-text{left:631px;top:1826px;width:330px;font-size:11px;line-height:20px;color:#3a3f4a}
.message-name{left:631px;top:1918px;font-weight:700;font-size:18px;color:var(--navy)}
.message-role{left:631px;top:1944px;font-size:8.5px;letter-spacing:1.2px;color:#c2c7d0}

/* map */
.map-band{left:0;top:2076px}

/* contact */
.contact-title{left:251px;top:2618px;font-weight:700;font-size:40px;color:var(--navy)}
.field{left:251px;width:343px;border:1px solid var(--line);font-size:9.5px;color:#a4a9b3;padding:5px 8px}
.send{left:251px;top:2805px;width:343px;height:25px;background:var(--navy);color:var(--white);font-size:10px;font-weight:500;display:flex;align-items:center;justify-content:center}
.info-head{font-size:10.5px;font-weight:700;color:#23262d;letter-spacing:.3px}
.info-line{font-size:10px;line-height:18px;color:#c0c4cc;white-space:nowrap}
.social{left:785px;top:2775px;display:flex;gap:9px}
.social span{width:26px;height:26px;border-radius:3px;background:#eef1f5;display:flex;align-items:center;justify-content:center}
.social span i{width:10px;height:10px;border-radius:50%;background:var(--navy);display:block}

/* footer */
.site-footer{left:0;top:2948px;width:1200px;height:149px;background:var(--navy);color:var(--white)}
.footer-bar{left:0;top:3097px;width:1200px;height:17px;background:var(--navy-deep);color:#d2d9e6;font-size:8px;display:flex;align-items:center;justify-content:center}
.f-head{font-size:9.5px;font-weight:700}
.f-text{font-size:8.5px;line-height:12px;color:#8e9ab3}
.f-links{font-size:8px;line-height:16px;font-weight:500}
.f-brand{left:286px;top:48px;width:100px;display:flex;flex-direction:column;align-items:center;gap:6px;font-family:"Montserrat",sans-serif;font-weight:600;font-size:10px;letter-spacing:1px;white-space:nowrap}
.f-brand i{width:20px;height:20px;background:var(--white);display:block}
.f-input{left:731px;top:66px;width:162px;height:23px;background:var(--white);border-radius:12px 0 0 12px;font-size:8.5px;color:#a4a9b3;padding:6px 10px}
.f-button{left:893px;top:66px;width:49px;height:23px;background:#8e939b;border-radius:0 12px 12px 0;font-size:8.5px;font-weight:700;display:flex;align-items:center;justify-content:center}
</style>
</head>
<body>

<header class="abs site-header">
  <a class="abs brand" href="#"><span class="brand-mark"></span>CORVELL LEGAL</a>
  <nav class="main-nav">
    <a class="current" href="#" style="left:490px;top:33px">HOME</a>
    <a href="#" style="left:561px;top:33px">ABOUT</a>
    <a href="#" style="left:637px;top:33px">SERVICES</a>
    <a href="#" style="left:726px;top:33px">CONTACT</a>
  </nav>
  <a class="abs cta-start" href="#">GET STARTED NOW!</a>
</header>

<svg class="abs hero-art" width="1200" height="460" viewBox="0 0 1200 460" role="img" aria-label="City office towers with the firm's principal lawyer in a suit">
  <defs>
    <linearGradient id="heroGrad" x1="0" y1="0" x2="1" y2="0.3">
      <stop offset="0" stop-color="#1f2a3a"/>
      <stop offset="0.4" stop-color="#3c4b5e"/>
      <stop offset="0.7" stop-color="#5c6c7e"/>
      <stop offset="1" stop-color="#2b3444"/>
    </linearGradient>
  </defs>
  <polygon points="0,0 1200,0 1200,359 311,457 0,332" fill="url(#heroGrad)"/>
</svg>

<section class="abs hero-copy">
  <div class="hero-kicker">WELCOME TO</div>
  <h1 class="hero-title">CORVELL LEGAL</h1>
  <div class="hero-tag">IT'S ABOUT RESULTS.</div>
  <p class="hero-text">We advise founders, boards and investors on deals, disputes and listings. Clear, commercial advice from an Adelaide firm built to get the outcome you need.</p>
</section>
<a class="abs btn btn-solid" href="#" style="left:257px;top:394px;width:86px">LEARN MORE</a>
<a class="abs btn btn-ghost" href="#" style="left:357px;top:394px;width:87px">CONTACT US</a>

<section>
  <div class="abs eyebrow" style="left:264px;top:614px">Learn More About</div>
  <h2 class="abs about-title">CORVELL LEGAL<br><span class="accent">WE GET RESULTS.</span></h2>
  <a class="abs btn btn-solid" href="#" style="left:263px;top:704px;width:90px">ABOUT US</a>
  <p class="abs about-text">We are a commercial law practice focused on outcomes. From first meeting to final signature we give clear, practical advice, keep costs transparent and stay close to the detail so your business can move forward with confidence and certainty.</p>
</section>

<svg class="abs services-band" width="1200" height="840" viewBox="0 0 1200 840" aria-hidden="true">
  <polygon points="0,113 1200,0 1200,729 0,839" fill="#1d3660"/>
</svg>
<section>
  <div class="abs services-head">
    <div class="eyebrow">Learn More About</div>
    <h2>Services</h2>
  </div>
  <div class="abs service-grid">
    <div class="service-photo" role="img" aria-label="Business meeting at a desk" style="background:linear-gradient(135deg,#2e2a28,#7a6a5a 55%,#cfc6b8)"></div>
    <div class="service-card"><h3>Business Law and Dispute Resolution</h3><p>Advice on contracts, disputes and negotiations that protects your interests and keeps your business moving.</p></div>
    <div class="service-photo" role="img" aria-label="Traveller holding a passport" style="background:linear-gradient(135deg,#2c4f8f,#4f72b0 50%,#e8e2d8)"></div>
    <div class="service-card"><h3>Corporate Transactions and Regulation</h3><p>Support for capital raisings, IPOs, mergers and compliance with market rules and regulators.</p></div>
    <div class="service-photo" role="img" aria-label="Pen signing a contract" style="background:linear-gradient(135deg,#e9e6e0,#c9c4bb 60%,#8d857a)"></div>
    <div class="service-card"><h3>Migration Assistance</h3><p>Guidance on business and skilled visas for owners, staff and investors coming to Australia.</p></div>
  </div>
  <a class="abs btn btn-ghost services-more" href="#">SEE ALL OUR SERVICES</a>
</section>

<section>
  <div class="abs message-frame"></div>
  <div class="abs message-photo" role="img" aria-label="Portrait of the principal lawyer with a night city skyline"></div>
  <svg class="abs quote-mark" width="24" height="18" viewBox="0 0 24 18" aria-hidden="true">
    <path d="M0 18V9C0 4 3 1 8 0l1 3C6 4 5 6 5 8h4v10zM14 18V9c0-5 3-8 8-9l1 3c-3 1-4 3-4 5h4v10z" fill="#c9ccd2"/>
  </svg>
  <p class="abs message-text">Starting this firm, I wanted clients to get senior attention on every matter. I work directly with you, explain options plainly and focus on the result that matters most to your business.</p>
  <div class="abs message-name">Marcus Hale</div>
  <div class="abs message-role">CORVELL LEGAL - CEO</div>
</section>

<svg class="abs map-band" width="1200" height="478" viewBox="0 0 1200 478">
  <g role="img" aria-label="Street map showing the office location in Adelaide">
    <polygon points="0,93 1200,0 1200,405 0,477" fill="#3b3b3d"/>
  </g>
  <rect x="498" y="176" width="202" height="19" fill="#ffffff"/>
  <polygon points="593,195 603,195 598,201" fill="#ffffff"/>
  <text x="505" y="189" font-family="Roboto,sans-serif" font-size="8" fill="#333">12 Harlow Square, Adelaide, South Australia</text>
  <text x="686" y="189" font-family="Roboto,sans-serif" font-size="9" fill="#666">×</text>
  <path d="M600 210c-6 0-10 4-10 10 0 7 10 18 10 18s10-11 10-18c0-6-4-10-10-10z" fill="#e0392b"/>
  <circle cx="600" cy="220" r="3.5" fill="#8e1d14"/>
</svg>

<section>
  <h2 class="abs contact-title">Get in touch</h2>
  <div class="abs field" style="top:2676px;height:25px">Name</div>
  <div class="abs field" style="top:2707px;height:25px">Email</div>
  <div class="abs field" style="top:2738px;height:60px">Message</div>
  <a class="abs send" href="#">Send</a>

  <div class="abs" style="left:612px;top:2683px">
    <div class="info-head">LOCATION</div>
    <div class="info-line" style="margin-top:6px">88 Harlow Street</div>
    <div class="info-line">Adelaide SA 5000</div>
    <div class="info-head" style="margin-top:6px">OUR HOURS</div>
    <div class="info-line" style="margin-top:6px">Mon-Fri: 09:00 – 18:00</div>
    <div class="info-line">Sat: 10:00 – 14:00</div>
  </div>
  <div class="abs" style="left:785px;top:2683px">
    <div class="info-head">CONTACT US</div>
    <div class="info-line" style="margin-top:6px">Phone: +61 8 8100 2040</div>
    <div class="info-line">Email: hello@corvell-legal.com</div>
    <div class="info-head" style="margin-top:6px">FOLLOW US</div>
  </div>
  <div class="abs social">
    <span aria-label="Social profile"><i></i></span>
    <span aria-label="Social profile"><i></i></span>
    <span aria-label="Social profile"><i></i></span>
    <span aria-label="Social profile"><i></i></span>
  </div>
</section>

<footer class="abs site-footer">
  <div class="abs f-brand"><i></i>CORVELL LEGAL</div>
  <div class="abs" style="left:432px;top:37px;width:140px">
    <div class="f-head">About Us</div>
    <p class="f-text" style="margin-top:9px">Corvell Legal advises businesses on transactions, disputes and migration from our office in Adelaide.</p>
  </div>
  <div class="abs" style="left:606px;top:37px">
    <div class="f-head">Useful Links</div>
    <div class="f-links" style="margin-top:6px">HOME<br>ABOUT<br>SERVICES<br>CONTACT</div>
  </div>
  <div class="abs" style="left:731px;top:37px">
    <div class="f-head">Subscribe To Our Newsletter</div>
    <p class="f-text" style="font-size:7.5px">Get our latest updates and legal news in your inbox.</p>
  </div>
  <div class="abs f-input">Email</div>
  <div class="abs f-button">Send</div>
</footer>
<div class="abs footer-bar">Copyright © 2018 Corvell Legal. All Rights Reserved.</div>

</body>
</html>
```